Marrowfield College Word Document Template

At the Marrowfield College, we want to offer our employees the ability to download branded word document templates that allow non-designers to create professional and on-brand documents. Through the use of theme preferences, locked elements and paragraph styles, the final deliverables should contain the brand elements identified at brand.marrowfield.example including the primary logo, fonts, and colors.

GENERAL TEMPLATE
A multi-functional document that contains a range of styles and brand elements that can be used broadly. The template should be flexible enough to work as a single-page document, or a multi-page document.

Target Market(s)

Administrative staff and faculty (Non-designers) who create documents largely for internal use

Font styles to use
Sans Serif
Other font styles liked:
• Fonts are attached – Roboto should be used predominantly with Antonio and Zilla available to use when appropriate. Fonts should default to Arial if fonts are not installed.

Colors
fbed22
ffffff
000000

Requirements
Must have
• REQUIREMENTS:
Use brand assets at brand.marrowfield.example (primary logo, fonts, colors are all available to download there).
If possible, fonts should default to Arial – if user does not have fonts installed.
Browse brand.marrowfield.example to get a sense of the established look and feel.
No elements should bleed off the page.
The final deliverable should be as locked down as possible. The logo should not be editable.

ELEMENTS TO INCLUDE:
Masthead to include: Primary logo and Placeholder for Unit name
Paragraph styles:
Document Title
Subhead 1
Subhead 2
Body
Bullets
Photo Placeholder
Pull Quote
Caption
Footer to include statement (small): the Marrowfield College prohibits discrimination in employment, educational programs, and activities on the basis of race, creed, color, religion, national origin, age, sex, pregnancy, disability, genetic information, status as a U.S. veteran, service in the U.S. military, sexual orientation, gender identity, associational preferences, or any other classification that deprives the person of consideration as an individual. The university also affirms its commitment to providing equal opportunities and equal access to university facilities. For additional information on nondiscrimination policies, contact the Director, Bureau of Fair Access and Inclusion, the Marrowfield College, 418 Penwick Hall, Iowa City, IA 52287-4493, 541-482-7163 (voice), 541-482-7190 (TDD), inclusion@marrowfield.example.
Nice to have
• Additional page templates for added flexibility would be nice...Such as a Cover sheet and/or Table of contents.

```html
<!DOCTYPE html>
<html lang="en">
<head>
<meta charset="utf-8">
<title>Marrowfield College Document Template Set</title>
<link rel="stylesheet" href="https://fonts.googleapis.com/css2?family=Roboto:wght@400;500;700;900&family=Roboto+Condensed:wght@700&display=swap">
<style>
:root{
  --gold:#fbed22;
  --gold-deep:#f5c518;
  --black:#000000;
  --white:#ffffff;
  --ink:#1a1a1a;
  --backdrop:#636363;
}
*{box-sizing:border-box;margin:0;padding:0}
html,body{width:1200px;height:1200px;overflow:hidden}
body{background:var(--backdrop);position:relative;font-family:"Roboto",Arial,sans-serif;color:var(--ink)}
.page{position:absolute;background:var(--white);overflow:hidden}
.wordmark{position:absolute;font-family:"Roboto",Arial,sans-serif;font-weight:900;color:var(--gold-deep);line-height:1;letter-spacing:0}
.unit-name{position:absolute;right:18px;font-size:6.5px;color:var(--ink)}
.doc-title{position:absolute;left:18px;font-family:"Roboto",Arial,sans-serif;font-weight:500;font-size:20px;color:var(--black);line-height:1}
.tab{position:absolute;left:18px;height:27px;padding:0 12px 0 10px;display:flex;align-items:center;font-weight:500;font-size:13px;clip-path:polygon(0 0,100% 0,95% 100%,0 100%)}
.tab-gold{background:var(--gold-deep);color:var(--black)}
.tab-black{background:var(--black);color:var(--gold-deep)}
.body-copy{position:absolute;font-size:6.6px;line-height:8.3px;color:var(--ink)}
.footer-notice{position:absolute;background:var(--black);color:var(--white);font-size:5.1px;line-height:6.4px;padding:8px 8px;letter-spacing:.15px}
.photo{position:absolute}
.cover-photo{left:12px;top:10px;width:339px;height:401px;background:linear-gradient(180deg,#3c63c9 0%,#7e9be0 30%,#b9b7b8 55%,#8e8a92 80%,#6e6a77 100%)}
.cover-band{position:absolute;left:12px;top:411px;width:339px;height:88px;background:var(--black)}
.cover-title{position:absolute;left:19px;top:423px;font-family:"Roboto Condensed",Arial,sans-serif;font-weight:700;font-size:24px;color:var(--gold-deep);line-height:1}
.cover-sub{position:absolute;left:19px;top:450px;width:320px;font-size:5.6px;line-height:7.2px;color:var(--gold-deep)}
.cover-url{position:absolute;left:0;right:0;top:481px;display:flex;justify-content:center;align-items:center;gap:6px;color:var(--white);font-size:7.5px;letter-spacing:1px}
.cover-url .dot{width:7px;height:7px;border-radius:50%;background:var(--gold-deep)}
.toc-heading{position:absolute;left:15px;top:66px;font-weight:500;font-size:16px;color:var(--black)}
.toc-item{position:absolute;left:148px;width:200px;display:flex;gap:8px}
.toc-num{font-weight:500;font-size:13px;line-height:1;color:var(--black);width:18px}
.toc-title{font-weight:500;font-size:10px;color:var(--black);line-height:1.1}
.toc-desc{font-size:5.2px;line-height:6.5px;color:#333;margin-top:3px;width:140px}
.toc-bar{position:absolute;left:12px;top:461px;width:165px;height:16px;background:var(--black)}
.bullet-col{position:absolute;width:150px;font-size:6.4px;line-height:8.2px}
.bullet-col li{list-style:none;position:relative;padding-left:7px;margin-bottom:10px}
.bullet-col li::before{content:"";position:absolute;left:0;top:3px;width:3px;height:3px;border-radius:50%;background:var(--black)}
.col-rule{position:absolute;width:1px;background:#bbb}
.quote-mark{position:absolute;left:0;right:0;display:flex;align-items:center;justify-content:center;gap:8px}
.quote-mark .rule{width:96px;height:1px;background:var(--gold-deep)}
.quote-text{position:absolute;font-size:6.6px;line-height:8.3px;text-align:center}
</style>
</head>
<body>

<section class="page cover" style="left:26px;top:68px;width:361px;height:506px">
  <div class="photo cover-photo" role="img" aria-label="Photo placeholder: historic domed campus building under a blue sky"></div>
  <div class="wordmark" style="left:13px;top:24px;font-size:28px">MARROWFIELD</div>
  <div class="cover-band"></div>
  <h1 class="cover-title">LOREM IPSUM DOLOR SIT AMET</h1>
  <p class="cover-sub">consectetur adipiscing elit, sed do eiusmod tempor incididunt ut labore et dolore magna aliqua. Ut enim ad minim veniam, quis nostrud exercitation</p>
  <div class="cover-url"><span class="dot"></span>brand.marrowfield.example</div>
</section>

<section class="page contents" style="left:415px;top:68px;width:362px;height:508px">
  <div class="wordmark" style="left:14px;top:24px;font-size:30px">MARROWFIELD</div>
  <div class="unit-name" style="top:37px">Department name</div>
  <h2 class="toc-heading">Table of Contents</h2>
  <div class="toc-item" style="top:110px"><span class="toc-num">01</span><div><div class="toc-title">Lorem ipsum dolor sit amet</div><p class="toc-desc">consectetur adipiscing elit, sed do eiusmod tempor incididunt ut labore et dolore magna aliqua.</p></div></div>
  <div class="toc-item" style="top:171px"><span class="toc-num">02</span><div><div class="toc-title">Lorem ipsum dolor sit amet</div><p class="toc-desc">consectetur adipiscing elit, sed do eiusmod tempor incididunt ut labore et dolore magna aliqua.</p></div></div>
  <div class="toc-item" style="top:236px"><span class="toc-num">03</span><div><div class="toc-title">Lorem ipsum dolor sit amet</div><p class="toc-desc">consectetur adipiscing elit, sed do eiusmod tempor incididunt ut labore et dolore magna aliqua.</p></div></div>
  <div class="toc-item" style="top:302px"><span class="toc-num">04</span><div><div class="toc-title">Lorem ipsum dolor sit amet</div><p class="toc-desc">consectetur adipiscing elit, sed do eiusmod tempor incididunt ut labore et dolore magna aliqua.</p></div></div>
  <div class="toc-item" style="top:365px"><span class="toc-num">05</span><div><div class="toc-title">Lorem ipsum dolor sit amet</div><p class="toc-desc">consectetur adipiscing elit, sed do eiusmod tempor incididunt ut labore et dolore magna aliqua.</p></div></div>
  <div class="toc-bar"></div>
</section>

<section class="page general" style="left:802px;top:68px;width:362px;height:508px">
  <div class="wordmark" style="left:18px;top:12px;font-size:17px">MARROWFIELD</div>
  <div class="unit-name" style="top:16px">Department name</div>
  <h2 class="doc-title" style="top:42px">DOCUMENT TITLE</h2>
  <div class="tab tab-gold" style="top:73px">SUBHEAD 1</div>
  <p class="body-copy" style="left:18px;top:110px;width:325px">Lorem ipsum dolor sit amet, consectetur adipiscing elit, sed do eiusmod tempor incididunt ut labore et dolore magna aliqua. Ut enim ad minim veniam, quis nostrud exercitation ullamco laboris nisi ut aliquip ex ea commodo consequat. Duis aute irure dolor in reprehenderit in voluptate velit esse cillum dolore eu fugiat nulla pariatur. Excepteur sint occaecat cupidatat non proident, sunt in culpa qui officia deserunt mollit anim id est laborum.</p>
  <div class="tab tab-black" style="top:166px">SUBHEAD 2</div>
  <p class="body-copy" style="left:18px;top:206px;width:328px">Lorem ipsum dolor sit amet, consectetur adipiscing elit, sed do eiusmod tempor incididunt ut labore et dolore magna aliqua. Ut enim ad minim veniam, quis nostrud exercitation ullamco laboris nisi ut aliquip ex ea commodo consequat. Duis aute irure dolor in reprehenderit in voluptate velit esse cillum dolore eu fugiat nulla pariatur. Excepteur sint occaecat cupidatat non proident, sunt in culpa qui officia deserunt mollit anim id est laborum.</p>
  <div class="tab tab-gold" style="top:265px;font-size:12.5px">SECTION TITLE</div>
  <ul class="bullet-col" style="left:19px;top:307px">
    <li>Lorem ipsum dolor sit amet, consectetur adipiscing elit, sed do eiusmod tempor incidi-</li>
    <li>Lorem ipsum dolor sit amet, consectetur adipiscing elit, sed do eiusmod tempor incididunt ut labore et dolore magna aliqua. Ut</li>
    <li>Lorem ipsum dolor sit amet, consectetur adipiscing elit, sed do eiusmod tempor incididunt ut labore et dolore magna aliqua. Ut enim ad minim veniam, quis nostrud exer-</li>
  </ul>
  <div class="col-rule" style="left:180px;top:306px;height:110px"></div>
  <ul class="bullet-col" style="left:190px;top:304px">
    <li>Lorem ipsum dolor sit amet, consectetur adipiscing elit, sed do eiusmod tempor incidi-</li>
    <li>Lorem ipsum dolor sit amet, consectetur adipiscing elit, sed do eiusmod tempor incididunt ut labore et dolore magna aliqua. Ut</li>
    <li>Lorem ipsum dolor sit amet, consectetur adipiscing elit, sed do eiusmod tempor incididunt ut labore et dolore magna aliqua. Ut enim ad minim veniam, quis nostrud exer-</li>
  </ul>
  <footer class="footer-notice" style="left:11px;top:429px;width:340px;height:69px">The Marrowfield College prohibits discrimination in employment, educational programs, and activities on the basis of race, creed, color, religion, national origin, age, sex, pregnancy, disability, genetic information, status as a U.S. veteran, service in the U.S. military, sexual orientation, gender identity, associational preferences, or any other classification that deprives the person of consideration as an individual. The university also affirms its commitment to providing equal opportunities and equal access to university facilities. For additional information on nondiscrimination policies, contact the Director, Bureau of Fair Access and Inclusion, the Marrowfield College, 418 Penwick Hall, Larchmont Falls, OR 97318-4493, 541-482-7163 (voice), 541-482-7190 (TDD), inclusion@marrowfield.example.</footer>
</section>

<section class="page inside-a" style="left:216px;top:626px;width:360px;height:507px">
  <div class="wordmark" style="left:18px;top:14px;font-size:17px">MARROWFIELD</div>
  <div class="unit-name" style="top:20px">Department name</div>
  <h2 class="doc-title" style="top:45px">FIRST ITEM</h2>
  <div class="tab tab-gold" style="top:74px">SECTION 1</div>
  <p class="body-copy" style="left:18px;top:108px;width:328px">Lorem ipsum dolor sit amet, consectetur adipiscing elit, sed do eiusmod tempor incididunt ut labore et dolore magna aliqua. Ut enim ad minim veniam, quis nostrud exercitation ullamco laboris nisi ut aliquip ex ea commodo consequat. Duis aute irure dolor in reprehenderit in voluptate velit esse cillum dolore eu fugiat nulla pariatur. Excepteur sint occaecat cupidatat non proident, sunt in culpa qui officia deserunt mollit anim id est laborum.</p>
  <div class="tab tab-black" style="top:161px">SECTION &nbsp;2</div>
  <p class="body-copy" style="left:18px;top:196px;width:328px">Lorem ipsum dolor sit amet, consectetur adipiscing elit, sed do eiusmod tempor incididunt ut labore et dolore magna aliqua. Ut enim ad minim veniam, quis nostrud exercitation ullamco laboris nisi ut aliquip ex ea commodo consequat. Duis aute irure dolor in reprehenderit in voluptate velit esse cillum dolore eu fugiat nulla pariatur. Excepteur sint occaecat cupidatat non proident, sunt in culpa qui officia deserunt mollit anim id est laborum.</p>
  <p class="body-copy" style="left:18px;top:251px;width:226px">Lorem ipsum dolor sit amet, consectetur adipiscing elit, sed do eiusmod tempor incididunt ut labore et dolore magna aliqua. Ut enim ad minim veniam, quis nostrud exercitation ullamco laboris nisi ut aliquip ex ea commodo consequat. Duis aute irure dolor in reprehenderit in voluptate velit esse cillum dolore eu fugiat nulla pariatur. Excepteur sint occaecat cupidatat non proident, sunt in culpa qui officia deserunt mollit anim id est laborum.</p>
  <div class="photo" style="left:248px;top:249px;width:97px;height:82px;background:linear-gradient(135deg,#2a1d14 0%,#6b4a33 55%,#d9a078 100%)" role="img" aria-label="Photo placeholder: graduate in cap and tassel at commencement"></div>
  <p class="body-copy" style="left:19px;top:322px;width:218px">Lorem ipsum dolor sit amet, consectetur adipiscing elit, sed do eiusmod tempor incididunt ut labore et dolore magna aliqua. Ut enim ad minim veniam, quis nostrud exercitation ullamco laboris nisi ut aliquip ex ea commodo consequat. Duis aute irure dolor in reprehenderit in</p>
  <p class="body-copy" style="left:18px;top:367px;width:218px">Lorem ipsum dolor sit amet, consectetur adipiscing elit, sed do eiusmod tempor incididunt ut labore et dolore magna aliqua. Ut enim ad minim veniam, quis nostrud exercitation ullamco laboris nisi ut aliquip ex ea commodo consequat. Duis aute irure dolor in reprehenderit in voluptate velit esse cillum dolore eu fugiat nulla pariatur. Excepteur sint occaecat cupidatat non proident, sunt in culpa qui officia deserunt mollit anim id est laborum.</p>
  <div class="photo" style="left:248px;top:347px;width:97px;height:81px;background:radial-gradient(circle at 45% 45%,#e8eef5 0%,#8fa3b8 30%,#3a4656 70%,#1c232c 100%)" role="img" aria-label="Photo placeholder: hands holding gears against a bright light"></div>
  <footer class="footer-notice" style="left:12px;top:437px;width:338px;height:62px;padding:6px 8px;font-size:4.9px;line-height:6.1px">The Marrowfield College prohibits discrimination in employment, educational programs, and activities on the basis of race, creed, color, religion, national origin, age, sex, pregnancy, disability, genetic information, status as a U.S. veteran, service in the U.S. military, sexual orientation, gender identity, associational preferences, or any other classification that deprives the person of consideration as an individual. The university also affirms its commitment to providing equal opportunities and equal access to university facilities. For additional information on nondiscrimination policies, contact the Director, Bureau of Fair Access and Inclusion, the Marrowfield College, 418 Penwick Hall, Larchmont Falls, OR 97318-4493, 541-482-7163 (voice), 541-482-7190 (TDD), inclusion@marrowfield.example.</footer>
</section>

<section class="page inside-b" style="left:635px;top:630px;width:361px;height:506px">
  <div class="wordmark" style="left:19px;top:15px;font-size:17px">MARROWFIELD</div>
  <div class="unit-name" style="top:16px">Department name</div>
  <h2 class="doc-title" style="top:47px">FIRST ITEM</h2>
  <div class="tab tab-gold" style="top:74px">SECTION 1</div>
  <p class="body-copy" style="left:18px;top:104px;width:228px">Lorem ipsum dolor sit amet, consectetur adipiscing elit, sed do eiusmod tempor incididunt ut labore et dolore magna aliqua. Ut enim ad minim veniam, quis nostrud exercitation ullamco laboris nisi ut aliquip ex ea commodo consequat. Duis aute irure dolor in reprehenderit in voluptate velit esse cillum dolore eu fugiat nulla pariatur. Excepteur sint occaecat cupidatat non proident, sunt in culpa qui officia deserunt mollit anim id est laborum.</p>
  <div class="photo" style="left:248px;top:78px;width:98px;height:82px;background:linear-gradient(180deg,#1d3f8a 0%,#4c6fae 45%,#8a6a55 75%,#3b2f2a 100%)" role="img" aria-label="Photo placeholder: student with a laptop outdoors at dusk"></div>
  <p class="body-copy" style="left:18px;top:171px;width:328px">Lorem ipsum dolor sit amet, consectetur adipiscing elit, sed do eiusmod tempor incididunt ut labore et dolore magna aliqua. Ut enim ad minim veniam, quis nostrud exercitation ullamco laboris nisi ut aliquip ex ea commodo consequat. Duis aute irure dolor in reprehenderit in voluptate velit esse cillum dolore eu fugiat nulla pariatur. Excepteur sint occaecat cupidatat non proident, sunt in culpa qui officia deserunt mollit anim id est laborum.</p>
  <div class="tab tab-black" style="top:219px">SECTION &nbsp;2</div>
  <p class="body-copy" style="left:18px;top:256px;width:328px">Lorem ipsum dolor sit amet, consectetur adipiscing elit, sed do eiusmod tempor incididunt ut labore et dolore magna aliqua. Ut enim ad minim veniam, quis nostrud exercitation ullamco laboris nisi ut aliquip ex ea commodo consequat. Duis aute irure dolor in reprehenderit in voluptate velit esse cillum dolore eu fugiat nulla pariatur. Excepteur sint occaecat cupidatat non proident, sunt in culpa qui officia deserunt mollit anim id est laborum.</p>
  <p class="body-copy" style="left:18px;top:304px;width:328px">Lorem ipsum dolor sit amet, consectetur adipiscing elit, sed do eiusmod tempor incididunt ut labore et dolore magna aliqua. Ut enim ad minim veniam, quis nostrud exercitation ullamco laboris nisi ut aliquip ex ea commodo consequat. Duis aute irure dolor in reprehenderit in voluptate velit esse cillum dolore eu fugiat nulla pariatur. Excepteur sint occaecat cupidatat non proident, sunt in culpa qui officia deserunt mollit anim id est laborum.</p>
  <div class="quote-mark" style="top:356px">
    <span class="rule"></span>
    <svg width="16" height="11" viewBox="0 0 16 11" aria-hidden="true"><path d="M0 11V6C0 2.5 2 .6 5.5 0l.6 1.6C4.2 2.2 3.3 3.3 3.2 5H6.5v6zM9 11V6c0-3.5 2-5.4 5.5-6l.6 1.6C13.2 2.2 12.3 3.3 12.2 5h3.3v6z" fill="#000"/></svg>
    <span class="rule"></span>
  </div>
  <blockquote class="quote-text" style="left:25px;top:375px;width:312px">Lorem ipsum dolor sit amet, consectetur adipiscing elit, sed do eiusmod tempor incididunt ut labore et dolore magna aliqua. Ut enim ad minim veniam, quis nostrud exercitation ullamco laboris nisi ut aliquip ex ea commodo consequat. Duis aute irure dolor in reprehenderit in voluptate velit esse cillum dolore eu fugiat nulla pariatur. Excepteur sint occaecat cupidatat non proident, sunt in culpa qui officia deserunt mollit anim id est laborum.</blockquote>
  <footer class="footer-notice" style="left:11px;top:431px;width:338px;height:65px;padding:7px 7px;font-size:4.9px;line-height:6.2px">The Marrowfield College prohibits discrimination in employment, educational programs, and activities on the basis of race, creed, color, religion, national origin, age, sex, pregnancy, disability, genetic information, status as a U.S. veteran, service in the U.S. military, sexual orientation, gender identity, associational preferences, or any other classification that deprives the person of consideration as an individual. The university also affirms its commitment to providing equal opportunities and equal access to university facilities. For additional information on nondiscrimination policies, contact the Director, Bureau of Fair Access and Inclusion, the Marrowfield College, 418 Penwick Hall, Larchmont Falls, OR 97318-4493, 541-482-7163 (voice), 541-482-7190 (TDD), inclusion@marrowfield.example.</footer>
</section>

</body>
</html>
```